Flyer YOga studio

I need a double sided DL flyer (landscape) with my yoga studio details on one side and my timetable on the back.

It looks like a lot of my info didn't save the orignal brief.

here is some information.

On the front side - Logo to be centred on white background.

Underneath text
$20 for 7 days unlimited yoga/pilates/run group
$99 for 1 month unlimited

also to be included - Location: Upstairs, 17 North Parade Linwood 3218
0438 915602
info@havenlinwood.com.au
www.havenlinwood.com.au

ON back side - Timetable only

Landscape

• Following text should be on front side

the logo
New clients offer: $20 for 7 days of Yoga
$99 - 1 month unlimited

Location: Upstairs, 17 North Parade
Linwood VIC 3218
info@havenlinwood.com.au/0438 915602

The following text:
Stretch...strength...Run
Any order you like...pick all or one. Only fear holds you back from experiencing any of these. We teach all our classes to what is happening in your body in this moment with an eye for alignment, correct muscle recruitment and breath awareness.

On the back:
Class descriptions:
Yoga: Flowing Vinyasa classes that heat the body through dynamic movements and slowing down for deep hip openers and relaxation.
Pilates: Mat classes for healthy bodies using a systematic sequencing of exercises that works the whole body, developing strength, flexibility and mindfulness.
Run groups: A non competitive session where you set the goals and we help you meet them, whether it getting to the corner and back or your first marathon.

```html
<!DOCTYPE html>
<html lang="en">
<head>
<meta charset="utf-8">
<title>Haven Yoga – Timetable</title>
<link rel="stylesheet" href="https://fonts.googleapis.com/css2?family=Arimo:wght@400;700&family=Carlito:wght@400&display=swap">
<style>
  :root {
    --paper: #ffffff;
    --ink: #111111;
    --rule: #a8a8a8;
    --flow-yellow: #f4f23e;
    --run-cyan: #c9f1f1;
    --flow-orange: #f8b232;
    --pilates-green: #92d14f;
    --express-lilac: #b3a6e4;
    --kids-magenta: #e23fe3;
    --heading-cyan: #4fd0de;
    --body-grey: #828d90;
    --band-grey: #59656c;
    --band-text: #ffffff;
    --name-text: #e3e6e8;
  }
  * { margin: 0; padding: 0; box-sizing: border-box; }
  html, body { width: 1200px; height: 583px; overflow: hidden; background: var(--paper); }
  .flyer { position: relative; width: 1200px; height: 583px; background: var(--paper); }

  .timetable {
    position: absolute; left: 40px; top: 35px; width: 672px;
    border-collapse: collapse; table-layout: fixed;
    border: 3px solid var(--ink);
    font-family: "Carlito", "Calibri", sans-serif; font-size: 10px; color: var(--ink);
  }
  .timetable td, .timetable th {
    border: 1px solid var(--rule); padding: 1px 2px;
    vertical-align: top; text-align: left; font-weight: 400;
    white-space: nowrap; overflow: hidden;
  }
  .timetable th { border-bottom: 2px solid var(--ink); }
  .timetable .time { border-right: 1px solid var(--ink); }
  .r-head th { height: 17px; }
  .r-s { height: 17px; }
  .r-930 { height: 45px; }
  .r-11 { height: 39px; }
  .r-gap { height: 41px; }
  .r-1215 { height: 39px; }
  .r-gap2 { height: 18px; }
  .r-4 { height: 25px; }
  .r-6 { height: 40px; }
  .r-715 { height: 40px; }
  .r-730 { height: 33px; }
  .yellow { background: var(--flow-yellow); }
  .cyan { background: var(--run-cyan); }
  .orange { background: var(--flow-orange); }
  .green { background: var(--pilates-green); }
  .lilac { background: var(--express-lilac); }
  .magenta { background: var(--kids-magenta); }
  .timetable td.bottom { vertical-align: bottom; }

  .classes {
    position: absolute; left: 734px; top: 32px; width: 420px;
    font-family: "Arimo", Arial, sans-serif; font-weight: 700;
    font-size: 21.5px; line-height: 23.6px; color: var(--body-grey);
    text-align: justify; text-align-last: center;
    hyphens: auto; -webkit-hyphens: auto;
  }
  .classes p { margin-bottom: 23.6px; }
  .classes .label { color: var(--heading-cyan); }

  .contact-band {
    position: absolute; left: 0; top: 478px; width: 1200px; height: 105px;
    background: var(--band-grey);
    font-family: "Arimo", Arial, sans-serif; font-weight: 700; color: var(--band-text);
  }
  .web { position: absolute; left: 0; width: 1034px; top: 6px; text-align: center; font-size: 34px; letter-spacing: 1px; }
  .reach { position: absolute; left: 0; width: 1010px; top: 48px; text-align: center; font-size: 34px; letter-spacing: 1px; }
  .brand-name {
    position: absolute; left: 968px; width: 200px; top: 38px; text-align: center;
    font-weight: 400; font-size: 20px; letter-spacing: 1px; color: var(--name-text);
  }
</style>
</head>
<body>
<main class="flyer">
  <table class="timetable">
    <colgroup>
      <col style="width:42px"><col style="width:90px"><col style="width:81px"><col style="width:97px">
      <col style="width:85px"><col style="width:92px"><col style="width:93px"><col style="width:92px">
    </colgroup>
    <tr class="r-head"><th class="time"></th><th>Monday</th><th>Tuesday</th><th>Wednesday</th><th>Thurs</th><th>Friday</th><th>Sat</th><th>Sunday</th></tr>
    <tr class="r-s"><td class="time">6.15am</td><td></td><td class="yellow">Flow (60)</td><td></td><td class="cyan">Run group</td><td class="yellow">Flow (60)</td><td></td><td></td></tr>
    <tr class="r-s"><td class="time">8am</td><td></td><td></td><td></td><td></td><td></td><td class="cyan">Run group - 7am</td><td></td></tr>
    <tr class="r-s"><td class="time"></td><td></td><td></td><td></td><td></td><td></td><td></td><td></td></tr>
    <tr class="r-930"><td class="time">9.30am</td><td class="orange">Flow (75 )</td><td class="orange">Flow (75 )</td><td class="orange">Flow (75 )</td><td class="orange">Flow (75 )</td><td class="orange">Flow (75 )</td><td class="orange">Flow (75 )</td><td class="orange">Flow (75 )</td></tr>
    <tr class="r-11"><td class="time">11am</td><td></td><td></td><td></td><td></td><td class="green">pilates - Open (60)</td><td></td><td></td></tr>
    <tr class="r-gap"><td class="time"></td><td></td><td></td><td></td><td></td><td></td><td></td><td></td></tr>
    <tr class="r-1215"><td class="time">12.15pm</td><td class="lilac">Express pilates</td><td></td><td class="lilac">Express Flow (45)</td><td></td><td class="lilac">Express Flow (45)</td><td></td><td></td></tr>
    <tr class="r-gap2"><td class="time"></td><td></td><td></td><td></td><td></td><td></td><td></td><td></td></tr>
    <tr class="r-4"><td class="time">4pm</td><td class="magenta">Kids yoga</td><td></td><td></td><td></td><td></td><td></td><td></td></tr>
    <tr class="r-6"><td class="time">6pm</td><td class="cyan bottom">Run group (6.15pm)</td><td class="green">pilates - Open (60)</td><td class="cyan bottom">Run group (6.15pm)</td><td class="yellow">Flow (60)</td><td></td><td></td><td></td></tr>
    <tr class="r-715"><td class="time">7.15pm</td><td></td><td class="orange">Flow (75)</td><td class="orange">Flow (75)</td><td class="green">pilates - Open (60)</td><td></td><td></td><td></td></tr>
    <tr class="r-730"><td class="time">7.30pm</td><td class="orange">Flow (75)</td><td></td><td></td><td></td><td></td><td></td><td></td></tr>
  </table>

  <section class="classes">
    <p><span class="label">Yoga:</span> Flowing Vinyasa classes that heat the body through dynamic movements and slowing down for deep hip openers and relaxation.</p>
    <p><span class="label">Pilates:</span> Mat classes for healthy bodies using a systematic sequencing of exercises that works the whole body, developing strength, flexibility and mindfulness.</p>
    <p><span class="label">Run groups:</span> A non competitive session where you set the goals and we help you meet them, whether it getting to the corner and back or your first marathon.</p>
  </section>

  <footer class="contact-band">
    <div class="web">www.havenlinwood.com.au</div>
    <div class="reach">0438 915602 | info@havenlinwood.com.au</div>
    <div class="brand-name">Haven Yoga</div>
  </footer>
</main>
</body>
</html>
```